Bref créative
Norland Equity Partners
Investing
Professional
Tom Radcliffe
President
728 Maplewood Ave. Suite 310
Oak Terrace, CA 90418
tom@NorlandEquityPartners.com
www.NorlandEquityPartners.com
We want our logo to be the main component of the card. Have fun and let me see what you got!
Feel free to try 1 or 2 sided card ideas.
Can use other fonts besides the logo font if you desire.

```html
<!DOCTYPE html>
<html lang="en">
<head>
<meta charset="utf-8">
<title>Norland Equity Partners – Business Card</title>
<link rel="stylesheet" href="https://fonts.googleapis.com/css2?family=Montserrat:wght@400;600;700&display=swap">
<style>
  :root {
    --bg: #e9e7e3;
    --card: #ffffff;
    --red: #e3262b;
    --ink: #1d1d1d;
    --grey: #6b6b6b;
    --rule: #2a2a2a;
  }
  html, body { margin: 0; padding: 0; overflow: hidden; }
  body {
    width: 1200px; height: 932px;
    background: var(--bg);
    font-family: "Montserrat", Arial, sans-serif;
    position: relative;
  }
  .card {
    position: absolute;
    width: 520px; height: 300px;
    background: var(--card);
    border-radius: 18px;
    box-shadow: 0 6px 18px rgba(0,0,0,.18);
    overflow: hidden;
  }
  .card--front { left: 70px; top: 180px; }
  .card--back { left: 610px; top: 452px; }
  .edge-red {
    position: absolute; right: 0; top: 28px;
    width: 9px; height: 110px; background: var(--red);
  }
  .edge-black {
    position: absolute; left: 0; bottom: 28px;
    width: 9px; height: 90px; background: var(--ink);
  }
  .holder { text-align: center; padding-top: 26px; }
  .holder__name {
    color: var(--red); font-weight: 700; font-size: 17px;
    letter-spacing: .5px; margin: 0; text-transform: uppercase;
  }
  .holder__title { color: var(--grey); font-size: 11px; margin: 3px 0 0; }
  .brand {
    display: flex; align-items: center; justify-content: center; gap: 10px;
    margin: 26px auto 0;
  }
  .brand__dot { width: 30px; height: 30px; border-radius: 50%; background: var(--red); }
  .brand__name {
    font-weight: 700; font-size: 20px; color: var(--ink); letter-spacing: .3px;
  }
  .brand-rule { width: 250px; height: 1px; background: var(--rule); margin: 12px auto 0; }
  .card--back .brand { margin-top: 102px; }
  .contacts {
    display: flex; flex-wrap: wrap; justify-content: center; gap: 6px 16px;
    margin: 26px 36px 0; font-size: 9.5px; color: var(--ink);
  }
  .contacts span { display: inline-flex; align-items: center; gap: 4px; }
  .contacts svg { width: 9px; height: 9px; fill: var(--red); }
  .contacts .web { color: var(--red); }
  .website {
    text-align: center; color: var(--red); font-weight: 600; font-size: 12px;
    margin-top: 22px;
  }
</style>
</head>
<body>
  <section class="card card--front">
    <div class="edge-red"></div>
    <div class="edge-black"></div>
    <header class="holder">
      <h1 class="holder__name">Tom Radcliffe</h1>
      <p class="holder__title">President</p>
    </header>
    <div class="brand">
      <div class="brand__dot"></div>
      <div class="brand__name">Norland Equity Partners</div>
    </div>
    <div class="brand-rule"></div>
    <div class="contacts">
      <span><svg viewBox="0 0 10 10"><path d="M5 0a3.5 3.5 0 0 0-3.5 3.5C1.5 6 5 10 5 10s3.5-4 3.5-6.5A3.5 3.5 0 0 0 5 0zm0 5a1.5 1.5 0 1 1 0-3 1.5 1.5 0 0 1 0 3z"/></svg>728 Maplewood Ave. Suite 310, Oak Terrace, CA 90418</span>
      <span><svg viewBox="0 0 10 10"><path d="M2 0l2 2.5-1 1.2a6 6 0 0 0 3.3 3.3l1.2-1L10 8l-1.5 2C4 10 0 6 0 1.5z"/></svg>555.014.2290</span>
      <span><svg viewBox="0 0 10 10"><path d="M0 2h10v6H0zM0 2l5 3.5L10 2" /></svg>tom@NorlandEquityPartners.com</span>
      <span class="web"><svg viewBox="0 0 10 10"><circle cx="5" cy="5" r="5"/></svg>www.NorlandEquityPartners.com</span>
    </div>
  </section>

  <section class="card card--back">
    <div class="edge-red"></div>
    <div class="edge-black"></div>
    <div class="brand">
      <div class="brand__dot"></div>
      <div class="brand__name">Norland Equity Partners</div>
    </div>
    <div class="brand-rule"></div>
    <div class="website">www.NorlandEquityPartners.com</div>
  </section>
</body>
</html>
```